K & M Wheel Depot business cards

need business card for tire/car care company based in tampa, florida. we sell used and new tires, also we service vehicles, tune ups, oil chasnge, brakes and A/c we offer free towing with major vehicle repair and tire purchase. we also offer free estimates on any engine or a/c repair. also we have the lowest price in the city on used and new tires.

Contact Information for Business Card

4170 E Marigold Blvd,
Tampa, Fl 33581
Ph: 813-572-3186
KandMWheelDepot@Mailverse.com

Font styles to use
Serif
Sans Serif
Decorative

Requirements
Must have
• my logo, what we do ( used and new tires , oil change, brakes, tune ups, free towing vehicl. Also business info.
Nice to have
• an image of a towing truck, highlighting that we offer free towing. something close to what i have in one of the attached image

```html
<!DOCTYPE html>
<html lang="en">
<head>
<meta charset="utf-8">
<title>K &amp; M Wheel Depot — Business Cards</title>
<link rel="stylesheet" href="https://fonts.googleapis.com/css2?family=Lato:wght@400;700&family=Montserrat:wght@400;600;700&display=swap">
<style>
  :root {
    --bg: #2b2b2b;
    --card: #ffffff;
    --card-shade: #ececec;
    --ink: #0a0a0a;
    --accent: #f2e600;
    --text: #2a2a2a;
    --muted: #555555;
    --link: #1f2a5c;
    --photo-a: #c9ccd2;
    --photo-b: #b3303a;
  }
  * { box-sizing: border-box; margin: 0; padding: 0; }
  html, body { width: 1200px; height: 873px; overflow: hidden; }
  body { background: var(--bg); font-family: "Lato", sans-serif; position: relative; }

  .card {
    position: absolute; width: 560px; height: 320px; overflow: hidden;
    background: linear-gradient(160deg, var(--card) 60%, var(--card-shade));
    box-shadow: 0 10px 30px rgba(0,0,0,.6);
  }
  .card--front { left: 40px; top: 60px; }
  .card--back { left: 600px; top: 493px; }

  /* shared bottom strip */
  .service-strip {
    position: absolute; left: 0; right: 0; bottom: 0; height: 56px;
    background: var(--ink); display: flex; align-items: center; justify-content: center;
    padding: 0 12px;
  }
  .service-strip::before, .service-strip::after {
    content: ""; position: absolute; left: 0; right: 0; height: 3px; background: var(--accent);
  }
  .service-strip::before { top: 8px; }
  .service-strip::after { bottom: 8px; }
  .service-strip__text {
    color: var(--accent); font-family: "Lato", sans-serif; font-weight: 700; font-size: 14px; white-space: nowrap;
  }

  .brand {
    position: absolute; display: flex; align-items: center; gap: 8px;
    font-family: "Montserrat", sans-serif; font-weight: 700; font-size: 18px; color: var(--ink);
  }
  .brand__dot { width: 14px; height: 14px; border-radius: 50%; background: var(--accent); border: 2px solid var(--ink); }

  /* front */
  .front__topband { position: absolute; left: 0; top: 0; width: 100%; height: 36px; background: var(--ink); }
  .front__topband::after { content: ""; position: absolute; left: 0; top: 0; width: 190px; height: 100%; background: var(--card); }
  .front__offer {
    position: absolute; left: 240px; top: 26px; width: 230px; height: 62px; background: var(--ink);
    color: var(--accent); font-family: "Montserrat", sans-serif; font-weight: 600; font-size: 12px;
    letter-spacing: .5px; line-height: 1.5; text-align: center; display: flex; align-items: center; justify-content: center; padding: 0 10px;
  }
  .front__photo {
    position: absolute; right: 18px; top: 100px; width: 176px; height: 140px;
    background: linear-gradient(120deg, var(--photo-a), var(--photo-b) 55%, #333);
    border-radius: 4px;
  }
  .front__brand { left: 28px; top: 100px; }
  .front__tow { position: absolute; left: 90px; top: 160px; color: var(--muted); }
  .front__tow-lead { font-size: 13px; letter-spacing: 5px; }
  .front__tow-main { font-size: 22px; letter-spacing: 5px; color: var(--text); margin-top: 6px; }
  .card--front .service-strip__text { font-weight: 400; font-size: 17px; }

  /* back */
  .back__nameband { position: absolute; left: 0; top: 58px; width: 100%; height: 104px; }
  .back__name { position: absolute; left: 40px; top: 86px; }
  .back__name-title { font-family: "Montserrat", sans-serif; font-weight: 700; font-size: 22px; color: var(--accent); }
  .back__name-role { font-family: "Lato", sans-serif; font-size: 15px; color: var(--accent); margin-left: 80px; }
  .back__brand { right: 24px; top: 28px; }
  .contact { position: absolute; left: 26px; top: 176px; list-style: none; }
  .contact__row { display: flex; align-items: center; gap: 12px; height: 28px; font-size: 15px; color: var(--text); }
  .contact__row--link { color: var(--link); }
  .contact__icon { width: 22px; height: 22px; flex: none; }
  .service-strip__sep { color: #dddddd; margin: 0 5px; }
</style>
</head>
<body>

<section class="card card--front" aria-label="Business card front">
  <div class="front__topband"></div>
  <div class="front__offer">LOWEST PRICE IN THE CITY ON USED AND NEW TIRES</div>
  <div class="front__photo" role="img" aria-label="Photo of a red flatbed tow truck carrying a car"></div>
  <div class="brand front__brand"><span class="brand__dot"></span>K &amp; M Wheel Depot</div>
  <div class="front__tow">
    <p class="front__tow-lead">WE OFFER</p>
    <p class="front__tow-main">FREE TOWING</p>
  </div>
  <div class="service-strip"><span class="service-strip__text">We also offer free estimates on any engine or a/c repair</span></div>
</section>

<section class="card card--back" aria-label="Business card back">
  <svg class="back__nameband" viewBox="0 0 560 104" preserveAspectRatio="none" aria-hidden="true">
    <polygon points="0,0 430,0 400,104 0,104" fill="var(--ink)"/>
    <polygon points="470,0 560,0 560,30 470,30" fill="var(--ink)"/>
  </svg>
  <div class="back__name">
    <p class="back__name-title">Daniel Voss</p>
    <p class="back__name-role">Owner / Founder</p>
  </div>
  <div class="brand back__brand"><span class="brand__dot"></span>K &amp; M Wheel Depot</div>

  <ul class="contact">
    <li class="contact__row contact__row--link">
      <svg class="contact__icon" viewBox="0 0 22 22" aria-hidden="true"><circle cx="11" cy="11" r="11" fill="var(--ink)"/><rect x="7.5" y="5" width="7" height="12" rx="1.5" fill="none" stroke="var(--accent)" stroke-width="1.6"/></svg>
      813-572-3186
    </li>
    <li class="contact__row contact__row--link">
      <svg class="contact__icon" viewBox="0 0 22 22" aria-hidden="true"><circle cx="11" cy="11" r="11" fill="var(--ink)"/><rect x="5.5" y="7" width="11" height="8" fill="var(--accent)"/><polyline points="5.5,7 11,11.5 16.5,7" fill="none" stroke="var(--ink)" stroke-width="1.2"/></svg>
      KandMWheelDepot@Mailverse.com
    </li>
    <li class="contact__row">
      <svg class="contact__icon" viewBox="0 0 22 22" aria-hidden="true"><circle cx="11" cy="11" r="11" fill="var(--ink)"/><path d="M11 17 C7 12 7 10 7 9 a4 4 0 0 1 8 0 c0 1 0 3 -4 8z" fill="var(--accent)"/><circle cx="11" cy="9" r="1.5" fill="var(--ink)"/></svg>
      4170 E Marigold Blvd, Tampa, Fl 33581
    </li>
  </ul>

  <div class="service-strip">
    <span class="service-strip__text">Brakes<span class="service-strip__sep">•</span>A/C Repair<span class="service-strip__sep">•</span>Engine tune-up<span class="service-strip__sep">•</span>Oil change<span class="service-strip__sep">•</span>Vehicle maintenance</span>
  </div>
</section>

</body>
</html>
```